Business Card Design

We would like a colorful, engaging, welcoming business card, utilizing our picture of a local lighthouse. We are a Church. We would like the design to mostly feature the colour blue.
Thank you so much to all Designers who sent in submissions to us - it was really hard to make a decision, they were all of such high quality. We would not hesitate to recommend Sketch Harbor to other churches/ businesses.
Kestrel Beacon Fellowship
Industry/Entity Type
Business
Contact Information for Business Card
Kestrel Beacon Fellowship Inc, 17 Merrow Rd, TALLOWVALE WA 6412, Ph: (08) 9517 4063, E: beaconfellowship@quorvex.example, Friendloop logo - Kestrel Beacon Fellowship Inc, Sunday Service 10am, "For God sent not his Son into the world to condemn the world; but that the world through Him might be saved." John 3:17.

```html
<!DOCTYPE html>
<html lang="en">
<head>
<meta charset="utf-8">
<title>Kestrel Beacon Fellowship Inc – Business Card</title>
<link rel="stylesheet" href="https://fonts.googleapis.com/css2?family=Cinzel:wght@400;700&family=Crimson+Text:wght@400;600&family=Tinos:ital,wght@0,700;1,400&family=Open+Sans:wght@700&display=swap">
<style>
  :root {
    --sky-deep: #0a1a5c;
    --sky-mid: #1d4fd6;
    --sky-glow: #6fa6ff;
    --hill-dark: #1b2124;
    --hill-green: #3f5a4a;
    --wave: #72c7ea;
    --white: #ffffff;
    --ink: #1b2850;
  }
  html, body {
    margin: 0;
    padding: 0;
    width: 1200px;
    height: 741px;
    overflow: hidden;
    background: #ffffff;
  }
  .card {
    position: relative;
    width: 1200px;
    height: 741px;
    overflow: hidden;
    background: var(--wave);
  }
  .scene {
    position: absolute;
    inset: 0;
    width: 1200px;
    height: 741px;
  }
  .verse {
    position: absolute;
    left: 520px;
    top: 108px;
    width: 600px;
    margin: 0;
    text-align: center;
    color: var(--white);
    font-family: "Tinos", "Times New Roman", serif;
    font-style: italic;
    font-size: 32px;
    line-height: 39px;
    letter-spacing: 0.5px;
    text-shadow: 0 1px 3px rgba(0,0,0,0.35);
  }
  .verse-ref {
    font-style: normal;
    font-weight: 700;
    font-size: 41px;
  }
  .org-name {
    position: absolute;
    left: 249px;
    top: 396px;
    margin: 0;
    color: var(--white);
    font-family: "Cinzel", serif;
    font-weight: 400;
    font-size: 29px;
    letter-spacing: 0.5px;
    white-space: nowrap;
    text-shadow: 0 2px 3px rgba(0,0,0,0.7);
  }
  .service-time {
    position: absolute;
    right: 262px;
    top: 434px;
    margin: 0;
    color: var(--white);
    font-family: "Tinos", "Times New Roman", serif;
    font-weight: 700;
    font-size: 11px;
    letter-spacing: 1px;
    text-shadow: 0 1px 2px rgba(0,0,0,0.7);
  }
  .social {
    position: absolute;
    left: 71px;
    top: 400px;
    width: 155px;
  }
  .social-photo {
    display: block;
    width: 155px;
    height: 155px;
    box-sizing: border-box;
    border: 4px solid var(--white);
    background: radial-gradient(circle at 50% 30%, #cfe4ff 0%, #5f97f0 30%, #1f4fc6 65%, #1b2a3a 100%);
  }
  .social-label {
    margin: 10px 0 0;
    color: var(--white);
    font-family: "Open Sans", sans-serif;
    font-weight: 700;
    font-size: 11.5px;
    letter-spacing: 0.2px;
    white-space: nowrap;
  }
  .contact {
    position: absolute;
    left: 700px;
    top: 532px;
    margin: 0;
    padding: 0;
    list-style: none;
    font-family: "Crimson Text", Georgia, serif;
    font-size: 21px;
    color: var(--ink);
  }
  .contact li {
    display: flex;
    align-items: center;
    height: 36px;
  }
  .contact-icon {
    width: 22px;
    height: 22px;
    margin-right: 24px;
    flex: none;
    fill: var(--white);
    color: var(--white);
  }
  .contact-at {
    width: 22px;
    margin-right: 24px;
    color: var(--white);
    font-family: "Open Sans", sans-serif;
    font-weight: 700;
    font-size: 19px;
    text-align: center;
  }
</style>
</head>
<body>
<main class="card">
  <svg class="scene" viewBox="0 0 1200 741" role="img" aria-label="Photograph of a stone lighthouse on a dark scrub-covered hilltop, its beam shining across a deep blue night sky">
    <defs>
      <radialGradient id="skyGlow" cx="0.34" cy="0.3" r="0.75">
        <stop offset="0" stop-color="#9cc2ff"/>
        <stop offset="0.18" stop-color="#3f7cf0"/>
        <stop offset="0.55" stop-color="#1d4fd6"/>
        <stop offset="1" stop-color="#0a1a5c"/>
      </radialGradient>
      <linearGradient id="hill" x1="0" y1="0" x2="0" y2="1">
        <stop offset="0" stop-color="#1b2124"/>
        <stop offset="0.6" stop-color="#2c3a36"/>
        <stop offset="1" stop-color="#4b6a56"/>
      </linearGradient>
    </defs>
    <rect class="sky" x="0" y="0" width="1200" height="520" fill="url(#skyGlow)"/>
    <path class="hill" d="M0 360 C120 330 230 310 330 312 C420 314 520 340 640 380 C760 420 900 440 1200 430 L1200 520 L0 520 Z" fill="url(#hill)"/>
    <path class="wave" d="M0 443 C150 470 300 506 440 506 C700 506 950 470 1200 427 L1200 741 L0 741 Z" fill="var(--wave)"/>
  </svg>

  <p class="verse">"For God sent not his Son into the world to condemn the world; but that the world through Him might be saved." <span class="verse-ref">John 3:17.</span></p>

  <h1 class="org-name">KESTREL BEACON FELLOWSHIP INC</h1>
  <p class="service-time">SUNDAY SERVICE 10AM</p>

  <div class="social">
    <span class="social-photo" role="img" aria-label="Small photo of the lighthouse glowing against a blue sky"></span>
    <p class="social-label">CATCH US ON FRIENDLOOP</p>
  </div>

  <ul class="contact">
    <li>
      <svg class="contact-icon" viewBox="0 0 24 24" aria-hidden="true">
        <path d="M11 0h2v3h2v2h-2v3l8 7h-2v9h-6v-6h-2v6H5v-9H3l8-7V5H9V3h2z"/>
      </svg>
      17 Merrow Rd, TALLOWVALE WA 6412
    </li>
    <li>
      <svg class="contact-icon" viewBox="0 0 24 24" aria-hidden="true">
        <path d="M2 7c0-2 3-3 10-3s10 1 10 3v2h-5V7H7v2H2z"/>
        <path d="M6 10h12l3 9H3z"/>
        <circle cx="12" cy="14.5" r="2.2" fill="var(--wave)"/>
      </svg>
      (08) 9517 4063
    </li>
    <li>
      <span class="contact-at" aria-hidden="true">@</span>
      beaconfellowship@quorvex.example
    </li>
  </ul>
</main>
</body>
</html>
```